International online gaming platform needs a game UI design

1. We need a game interface for three kinds of theme based on our guideline and sample mockup.
2. The product type is the online casino games related, we need a series of casino games UIs, however, we can start on the game lobby first.
3. Three theme you might choose from or refer to:
A. 3D look & feel
B. Realistic casino theme
C. Richness and grandeur
D. European casino style
4. NOT ALLOWED to change the design layout.
MUST follow our sample mock up and ONLY redefine the design style.
5. All items must be in a stand-alone component, eg. Button, Tab, Icon,... etc.
6. We need the layout in vector shape, but we can review in JPG or PNG format.
7. The image size: 1366 x 768

Updated:
1. All items and their positions should be same as the sample UI we provided.
Please redesign all the items and create a new theme for it.
No need to create a new layout.
2. Although we accept the draft design, but all the items in UI should be completed.
3. All the wordings in the sample UI are confirmed, you might change the fonts.
4. For the avatar in the left hand side, you don't have to redraw it.
We already have our own avatar system implemented.
5. All the items such as icons, tabs, and buttons are free to redesign.

Dear designers,

We've increased our budget and raise the prize money to 800 USD.  
We also accept the draft design in PNG format and we can go through the details in handover stage.
Thank you very much. 

Reason: Dear designers, We decided to extend the deadline by 7 days. As mentioned in the task description, we are looking for a new style of design and you might refer to the below style. A. 3D look & feel B. Realistic casino theme C. Richness and grandeur D. European casino style If you are still interested in our project, please send us your work. Thank you very much!

Casino

```html
<!DOCTYPE html>
<html lang="en">
<head>
<meta charset="utf-8">
<title>Live Casino Lobby</title>
<link rel="stylesheet" href="https://fonts.googleapis.com/css2?family=Arimo:wght@400;700&display=swap">
<style>
:root{
  --red:#e2231a;
  --red-dark:#7d0b08;
  --red-mid:#b3120d;
  --gold:#f2c230;
  --gold-dark:#a87810;
  --yellow:#ffe12a;
  --green:#118a1c;
  --green-dark:#0a5410;
  --felt:#0f3d1a;
  --ink:#0d0d0d;
  --white:#ffffff;
  --grid:#d8d8d8;
  --blue:#1630d8;
  --orange:#f7a21b;
  --font:"Arimo", Arial, sans-serif;
}
*{box-sizing:border-box;margin:0;padding:0}
html,body{width:1200px;height:675px;overflow:hidden;background:#000}
body{font-family:var(--font)}
.stage{position:relative;width:1366px;height:768px;transform:scale(0.878477);transform-origin:0 0;
  background:radial-gradient(ellipse at 70% 10%,#2f7a33 0%,#12461d 45%,#07200c 100%);overflow:hidden}
.abs{position:absolute}
.scene{left:0;top:0;width:1366px;height:768px;background:radial-gradient(ellipse 520px 200px at 950px 40px,rgba(190,140,60,.35),transparent 70%)}

/* header */
.brand{left:16px;top:8px;display:flex;align-items:center;height:40px}
.brand-name{font-size:38px;font-weight:700;color:var(--yellow);letter-spacing:1px;line-height:1}
.tools{right:10px;top:8px;display:flex;gap:8px}
.tool{width:31px;height:31px;border-radius:4px;background:linear-gradient(#ffe57a,#d39b12);border:1px solid #6a4a05;display:flex;align-items:center;justify-content:center}
.tool.close{background:linear-gradient(#ff5a3a,#b3120d)}
.clock{left:10px;top:62px;width:292px;height:46px;border-radius:6px;background:linear-gradient(#27b52f,var(--green-dark));border:1px solid #064b0b;color:var(--white);font-size:20px;display:flex;align-items:center;justify-content:center}
.tab{top:54px;height:58px;border:2px solid var(--gold);border-radius:6px;background:linear-gradient(#c3180f,var(--red-dark));display:flex;align-items:center;justify-content:center;color:var(--yellow);font-size:27px;font-weight:700;padding-left:60px}
.tab-art{position:absolute;left:-2px;top:-6px;width:66px;height:66px;border-radius:50%;background:radial-gradient(#fff6d0,#c89a2c);border:3px solid #d9b04a}

/* player panel */
.player{left:10px;top:123px;width:214px;height:604px;border:2px solid var(--gold);border-radius:6px;background:linear-gradient(#4a0806,#2a0303);overflow:hidden}
.avatar{left:28px;top:22px;width:154px;height:182px;border:3px solid #8a2a10;border-radius:6px;background:linear-gradient(#21496e,#0f2640)}
.username{left:0;top:212px;width:210px;text-align:center;color:var(--yellow);font-size:18px}
.profile-btn{left:16px;top:246px;width:178px;height:44px;border-radius:5px;background:linear-gradient(#ffc44a,var(--orange));border:1px solid #a86200;color:#3a1500;font-size:20px;display:flex;align-items:center;justify-content:center}
.menu-btn{left:14px;width:180px;height:46px;border-radius:4px;border:1px solid #a0170f;background:linear-gradient(#8a0f0a,#4a0403);color:var(--orange);font-size:16px;display:flex;align-items:center;gap:8px;padding-left:8px;white-space:nowrap}
.menu-ico{width:22px;height:22px;border-radius:3px;background:linear-gradient(#ffe57a,#d39b12);display:flex;align-items:center;justify-content:center;font-weight:700;font-size:14px;color:#111;flex:none}
.panel-art{left:0;top:468px;width:210px;height:134px;background:linear-gradient(160deg,#1e5a2b,#7a1a14 60%,#e8e0d0)}

/* dealer roads */
.feature{left:245px;top:126px;width:317px;height:154px;border:3px solid var(--gold);border-radius:6px;background:#5a0704}
.road-card{border-radius:6px;background:linear-gradient(#c9c9c9,#6d6d6d);border:1px solid #111}
.dealer-pic{background:linear-gradient(#2f6a90,#0e2c44);border:2px solid var(--gold-dark)}
.road{background:#fff}
.name-bar{background:#0b0b0b;border:1px solid #999;border-radius:3px;color:var(--white);display:flex;justify-content:space-between;align-items:center;overflow:hidden}
.name-bar span{padding:0 8px}
.name-bar .deals{background:#8a0a0a;height:100%;display:flex;align-items:center}
.rack{left:568px;top:127px;width:778px;height:145px;border:3px solid var(--orange);border-radius:6px;background:#7a3a05}

/* filter bar */
.filters{left:248px;top:285px;width:1098px;height:48px;border:2px solid #8a6a12;border-radius:5px;background:#1d1a0c}
.fbtn{top:5px;height:35px;border-radius:4px;border:1px solid #7a5b05;background:linear-gradient(#ffe06a,#e0a915);color:#1a1000;font-size:18px;display:flex;align-items:center;justify-content:center;gap:6px}
.fbtn.big{font-size:21px;font-weight:700}

/* tables */
.table{width:350px;height:188px;border:2px solid var(--red);border-radius:6px;background:linear-gradient(#d21a10,#8e0b07);overflow:hidden}
.table-head{left:0;top:0;width:346px;height:42px;background:linear-gradient(#17a01f,var(--green-dark));color:var(--white);font-size:12.5px;font-weight:700}
.table-head .t{position:absolute;left:12px;top:6px}
.table-head .lim{position:absolute;left:12px;top:25px;color:#ffe12a;font-weight:400}
.table-head .c{position:absolute;right:10px;top:5px}
.table-head .n{position:absolute;right:10px;top:23px;color:#ffe12a}
.join{left:108px;top:18px;width:124px;height:50px;border-radius:5px;background:linear-gradient(#d8281e,#7d0b08);border:2px solid #5a0402;box-shadow:0 2px 0 #2a0000;color:var(--white);font-size:24px;font-weight:700;display:flex;align-items:center;justify-content:center;z-index:2}
.seats{left:0;top:142px;width:346px;height:42px;background:#0a0a0a}
.drop{top:5px;width:48px;height:33px;border-radius:3px;background:linear-gradient(#f24a38,#b3120d);display:flex;align-items:center;justify-content:center}

/* balance */
.balance-bar{left:10px;top:733px;width:1346px;height:33px;border-radius:4px;background:linear-gradient(#8a0c08,#3a0302);display:flex;align-items:center;justify-content:flex-end;gap:6px;padding-right:16px}
.balance-label{color:#d9d9d9;font-size:19px;font-weight:700;margin-right:4px}
.cur{background:#111;border:1px solid #999;border-radius:3px;color:var(--white);font-size:15px;font-weight:700;padding:2px 4px;display:flex;align-items:center;gap:4px}
.cur i{display:inline-block;background:#c3180f;padding:0 4px;font-style:normal}
.amount{width:140px;height:26px;background:#0b0b0b;border-radius:3px;color:var(--white);font-size:17px;display:flex;align-items:center;justify-content:center}
</style>
</head>
<body>
<div class="stage">
  <div class="abs scene" role="img" aria-label="Casino roulette table backdrop on green felt"></div>

  <div class="abs brand"><span class="brand-name">LIVE CASINO</span></div>
  <div class="abs tools">
    <span class="tool"><svg width="18" height="18"><rect x="2" y="2" width="14" height="14" fill="none" stroke="#222" stroke-width="2"/><text x="9" y="14" font-size="11" text-anchor="middle" font-family="Arimo">$</text></svg></span>
    <span class="tool"><svg width="18" height="18"><rect x="2" y="2" width="14" height="14" fill="none" stroke="#222" stroke-width="2"/><circle cx="9" cy="9" r="4" fill="none" stroke="#222" stroke-width="2"/></svg></span>
    <span class="tool"><svg width="18" height="18"><path d="M6 14V3l9-2v11" fill="none" stroke="#222" stroke-width="2"/><circle cx="4.5" cy="14" r="2.5"/><circle cx="13.5" cy="12" r="2.5"/></svg></span>
    <span class="tool"><svg width="18" height="18" fill="none" stroke="#222" stroke-width="2"><path d="M2 7V2h5M11 2h5v5M16 11v5h-5M7 16H2v-5"/></svg></span>
    <span class="tool close"><svg width="16" height="16" stroke="#fff" stroke-width="3"><path d="M3 3l10 10M13 3L3 13"/></svg></span>
  </div>

  <div class="abs clock">1/28/2014 06:54 PM GMT +8</div>
  <div class="abs tab" style="left:322px;width:240px"><span class="tab-art" role="img" aria-label="Playing cards and chips emblem"></span>Baccarat</div>
  <div class="abs tab" style="left:580px;width:237px"><span class="tab-art" role="img" aria-label="Dealer emblem"></span>Super six</div>
  <div class="abs tab" style="left:836px;width:254px"><span class="tab-art" role="img" aria-label="Roulette wheel emblem"></span>Roultee</div>
  <div class="abs tab" style="left:1106px;width:250px"><span class="tab-art" role="img" aria-label="Dice emblem"></span>Sic Bo</div>

  <aside class="abs player">
    <div class="abs avatar" role="img" aria-label="Player avatar"></div>
    <div class="abs username">ALPos 848767</div>
    <div class="abs profile-btn">Profile</div>
    <div class="abs menu-btn" style="top:316px"><span class="menu-ico">&#9656;</span>Announcements</div>
    <div class="abs menu-btn" style="top:367px"><span class="menu-ico">!</span>Rules &amp; Regulation</div>
    <div class="abs menu-btn" style="top:416px"><span class="menu-ico">?</span>Quick tour</div>
    <div class="abs panel-art" role="img" aria-label="Casino chips and playing cards illustration"></div>
  </aside>

  <section class="abs feature">
    <div class="abs road-card" style="left:6px;top:4px;width:300px;height:136px;background:linear-gradient(#fff,#e0e0e0)"></div>
    <div class="abs dealer-pic" style="left:11px;top:9px;width:96px;height:100px" role="img" aria-label="Dealer photo"></div>
    <svg class="abs road" style="left:112px;top:8px" width="190" height="98">
      <defs><pattern id="cellA" width="14" height="14" patternUnits="userSpaceOnUse"><path d="M14 0H0V14" fill="none" stroke="#d0d0d0"/></pattern></defs>
      <rect width="190" height="98" fill="url(#cellA)"/>
      <g fill="none" stroke-width="2">
        <circle cx="7" cy="7" r="5.5" stroke="var(--blue)"/><circle cx="7" cy="21" r="5.5" stroke="var(--blue)"/><circle cx="21" cy="7" r="5.5" stroke="var(--red)"/><circle cx="21" cy="21" r="5.5" stroke="var(--red)"/>
        <circle cx="35" cy="7" r="5.5" stroke="var(--blue)"/><circle cx="49" cy="7" r="5.5" stroke="var(--red)"/><circle cx="63" cy="7" r="5.5" stroke="var(--blue)"/><circle cx="77" cy="7" r="5.5" stroke="var(--red)"/>
        <circle cx="91" cy="7" r="5.5" stroke="var(--red)"/><circle cx="105" cy="7" r="5.5" stroke="var(--red)"/><circle cx="119" cy="7" r="5.5" stroke="var(--blue)"/><circle cx="133" cy="7" r="5.5" stroke="var(--blue)"/>
        <circle cx="133" cy="21" r="5.5" stroke="var(--blue)"/><circle cx="133" cy="35" r="5.5" stroke="var(--blue)"/><circle cx="147" cy="7" r="5.5" stroke="var(--red)"/><circle cx="147" cy="21" r="5.5" stroke="var(--red)"/>
        <circle cx="147" cy="35" r="5.5" stroke="var(--red)"/><circle cx="147" cy="49" r="5.5" stroke="var(--red)"/><circle cx="147" cy="63" r="5.5" stroke="var(--red)"/><circle cx="147" cy="77" r="5.5" stroke="var(--red)"/>
        <circle cx="161" cy="7" r="5.5" stroke="var(--blue)"/><circle cx="161" cy="21" r="5.5" stroke="var(--blue)"/>
      </g>
      <g fill="var(--blue)"><circle cx="11" cy="11" r="2.5"/><circle cx="39" cy="11" r="2.5"/><circle cx="151" cy="39" r="2.5"/></g>
    </svg>
    <div class="abs name-bar" style="left:11px;top:113px;width:294px;height:25px;font-size:14px"><span>Dealer Name</span><span class="deals">Deals 999</span></div>
  </section>

  <section class="abs rack">
    <div class="abs road-card" style="left:9px;top:14px;width:242px;height:110px"></div>
    <div class="abs road-card" style="left:265px;top:14px;width:242px;height:110px"></div>
    <div class="abs road-card" style="left:520px;top:14px;width:242px;height:110px"></div>

    <div class="abs dealer-pic" style="left:15px;top:20px;width:76px;height:76px" role="img" aria-label="Dealer photo"></div>
    <svg class="abs road" style="left:94px;top:20px" width="150" height="76">
      <defs><pattern id="cellB" width="12.5" height="12.5" patternUnits="userSpaceOnUse"><path d="M12.5 0H0V12.5" fill="none" stroke="#d0d0d0"/></pattern></defs>
      <rect width="150" height="76" fill="url(#cellB)"/>
      <g fill="none" stroke-width="1.6"><circle cx="6" cy="6" r="4.5" stroke="var(--blue)"/><circle cx="6" cy="18.5" r="4.5" stroke="var(--blue)"/><circle cx="18.5" cy="6" r="4.5" stroke="var(--red)"/><circle cx="31" cy="6" r="4.5" stroke="var(--blue)"/><circle cx="43.5" cy="6" r="4.5" stroke="var(--red)"/><circle cx="56" cy="6" r="4.5" stroke="var(--blue)"/></g>
    </svg>
    <div class="abs name-bar" style="left:15px;top:100px;width:232px;height:19px;font-size:11px"><span>Dealer Name</span><span class="deals">Deals 999</span></div>

    <div class="abs dealer-pic" style="left:271px;top:20px;width:76px;height:76px" role="img" aria-label="Dealer photo"></div>
    <svg class="abs road" style="left:350px;top:20px" width="150" height="76">
      <rect width="150" height="76" fill="url(#cellB)"/>
      <g fill="none" stroke-width="1.6"><circle cx="6" cy="6" r="4.5" stroke="var(--blue)"/><circle cx="6" cy="18.5" r="4.5" stroke="var(--blue)"/><circle cx="6" cy="31" r="4.5" stroke="var(--blue)"/><circle cx="18.5" cy="6" r="4.5" stroke="var(--red)"/><circle cx="31" cy="6" r="4.5" stroke="var(--blue)"/><circle cx="43.5" cy="6" r="4.5" stroke="var(--red)"/><circle cx="56" cy="6" r="4.5" stroke="var(--blue)"/><circle cx="68.5" cy="6" r="4.5" stroke="var(--red)"/><circle cx="81" cy="6" r="4.5" stroke="var(--blue)"/><circle cx="93.5" cy="6" r="4.5" stroke="var(--blue)"/></g>
    </svg>
    <div class="abs name-bar" style="left:271px;top:100px;width:232px;height:19px;font-size:11px"><span>Dealer Name</span><span class="deals">Deals 999</span></div>

    <div class="abs dealer-pic" style="left:526px;top:20px;width:76px;height:76px" role="img" aria-label="Dealer photo"></div>
    <svg class="abs road" style="left:605px;top:20px" width="150" height="76">
      <rect width="150" height="76" fill="url(#cellB)"/>
      <g fill="none" stroke-width="1.6"><circle cx="6" cy="6" r="4.5" stroke="var(--blue)"/><circle cx="18.5" cy="6" r="4.5" stroke="var(--red)"/><circle cx="31" cy="6" r="4.5" stroke="var(--blue)"/><circle cx="43.5" cy="6" r="4.5" stroke="var(--red)"/><circle cx="43.5" cy="18.5" r="4.5" stroke="var(--red)"/><circle cx="56" cy="6" r="4.5" stroke="var(--blue)"/><circle cx="68.5" cy="6" r="4.5" stroke="var(--red)"/><circle cx="81" cy="6" r="4.5" stroke="var(--red)"/><circle cx="93.5" cy="6" r="4.5" stroke="var(--blue)"/><circle cx="106" cy="6" r="4.5" stroke="var(--blue)"/><circle cx="106" cy="18.5" r="4.5" stroke="var(--blue)"/><circle cx="106" cy="31" r="4.5" stroke="var(--blue)"/></g>
    </svg>
    <div class="abs name-bar" style="left:526px;top:100px;width:232px;height:19px;font-size:11px"><span>Dealer Name</span><span class="deals">Deals 999</span></div>
  </section>

  <nav class="abs filters">
    <div class="abs fbtn" style="left:7px;width:155px">Multiplayer
      <svg width="40" height="24"><circle cx="20" cy="7" r="5"/><path d="M11 22a9 8 0 0 1 18 0z"/><circle cx="9" cy="9" r="4"/><path d="M1 22a8 7 0 0 1 13-5v5z"/><circle cx="31" cy="9" r="4"/><path d="M39 22a8 7 0 0 0-13-5v5z"/></svg></div>
    <div class="abs fbtn big" style="left:507px;width:113px">JOIN ANY</div>
    <div class="abs fbtn" style="left:623px;width:52px;font-weight:700">A&#10140;Z</div>
    <div class="abs fbtn" style="left:679px;width:52px;font-weight:700">$<svg width="10" height="12"><path d="M2 0h6v6h2L5 12 0 6h2z"/></svg></div>
    <div class="abs fbtn" style="left:735px;width:52px;font-weight:700">$<svg width="10" height="12"><path d="M2 12h6V6h2L5 0 0 6h2z"/></svg></div>
    <div class="abs fbtn" style="left:791px;width:53px"><svg width="38" height="22"><g><circle cx="6" cy="6" r="3.5"/><circle cx="15" cy="6" r="3.5"/><circle cx="24" cy="6" r="3.5"/><circle cx="33" cy="6" r="3.5"/><rect x="2" y="11" width="8" height="10" rx="2"/><rect x="11" y="11" width="8" height="10" rx="2"/><rect x="20" y="11" width="8" height="10" rx="2"/><rect x="29" y="11" width="8" height="10" rx="2"/></g></svg></div>
    <div class="abs fbtn" style="left:848px;width:52px">&le;3</div>
    <div class="abs fbtn" style="left:904px;width:52px">3&nbsp;&gt;</div>
    <div class="abs fbtn" style="left:959px;width:128px">All Limits <svg width="14" height="10"><path d="M0 0h14L7 10z"/></svg></div>
  </nav>

  <svg width="0" height="0" style="position:absolute">
    <defs>
      <g id="felt">
        <polygon points="36,0 314,0 331,84 19,84" fill="#151515" stroke="#555" stroke-width="1.5"/>
        <polygon points="32,36 318,36 331,84 19,84" fill="#260606"/>
        <line x1="29" y1="60" x2="322" y2="60" stroke="#c3180f"/>
        <line x1="32" y1="36" x2="318" y2="36" stroke="#c3180f"/>
        <g stroke="#c3180f"><line x1="66" y1="36" x2="62" y2="84"/><line x1="102" y1="36" x2="99" y2="84"/><line x1="138" y1="36" x2="137" y2="84"/><line x1="175" y1="36" x2="175" y2="84"/><line x1="212" y1="36" x2="213" y2="84"/><line x1="248" y1="36" x2="251" y2="84"/><line x1="284" y1="36" x2="288" y2="84"/></g>
        <g font-family="Arimo, sans-serif" font-size="15" font-style="italic" text-anchor="middle">
          <g fill="#c3180f"><text x="47" y="54">B</text><text x="84" y="54">B</text><text x="120" y="54">B</text><text x="157" y="54">B</text><text x="194" y="54">B</text><text x="231" y="54">B</text><text x="268" y="54">B</text><text x="303" y="54">B</text></g>
          <g fill="#e8c020"><text x="42" y="79">p</text><text x="81" y="79">p</text><text x="118" y="79">p</text><text x="156" y="79">p</text><text x="194" y="79">p</text><text x="232" y="79">p</text><text x="270" y="79">p</text><text x="308" y="79">p</text></g>
        </g>
      </g>
      <g id="seat" fill="#f2c64a"><circle cx="0" cy="-6" r="7"/><path d="M-16 12a16 11 0 0 1 32 0z" fill="#7fb6e6"/></g>
      <g id="seatrow">
        <use href="#seat" x="34" y="20"/><use href="#seat" x="80" y="20"/><use href="#seat" x="125" y="20"/><use href="#seat" x="169" y="20"/><use href="#seat" x="211" y="20"/>
      </g>
      <path id="down" d="M2 4h24L14 18z" fill="#4a0303"/>
    </defs>
  </svg>

  <article class="abs table" style="left:249px;top:343px">
    <div class="abs table-head"><span class="t">Baccart A5-3C</span><span class="lim">Bet Limit</span><span class="c">Commission 0/7</span><span class="n">0/100</span></div>
    <div class="abs join">JOIN</div>
    <svg class="abs" style="left:0;top:54px" width="350" height="86"><use href="#felt"/></svg>
    <div class="abs seats"><svg class="abs" style="left:0;top:4px" width="230" height="36"><use href="#seatrow"/></svg><span class="abs drop" style="left:241px"><svg width="28" height="20"><use href="#down"/></svg></span><span class="abs drop" style="left:292px"><svg width="28" height="20"><use href="#down"/></svg></span></div>
  </article>
  <article class="abs table" style="left:622px;top:343px">
    <div class="abs table-head"><span class="t">Baccart A5-3C</span><span class="lim">Bet Limit</span><span class="c">Commission 0/7</span><span class="n">0/100</span></div>
    <div class="abs join">JOIN</div>
    <svg class="abs" style="left:0;top:54px" width="350" height="86"><use href="#felt"/></svg>
    <div class="abs seats"><svg class="abs" style="left:0;top:4px" width="230" height="36"><use href="#seatrow"/></svg><span class="abs drop" style="left:241px"><svg width="28" height="20"><use href="#down"/></svg></span><span class="abs drop" style="left:292px"><svg width="28" height="20"><use href="#down"/></svg></span></div>
  </article>
  <article class="abs table" style="left:994px;top:343px">
    <div class="abs table-head"><span class="t">Baccart A5-3C</span><span class="lim">Bet Limit</span><span class="c">Commission 0/7</span><span class="n">0/100</span></div>
    <div class="abs join">JOIN</div>
    <svg class="abs" style="left:0;top:54px" width="350" height="86"><use href="#felt"/></svg>
    <div class="abs seats"><svg class="abs" style="left:0;top:4px" width="230" height="36"><use href="#seatrow"/></svg><span class="abs drop" style="left:241px"><svg width="28" height="20"><use href="#down"/></svg></span><span class="abs drop" style="left:292px"><svg width="28" height="20"><use href="#down"/></svg></span></div>
  </article>
  <article class="abs table" style="left:249px;top:540px">
    <div class="abs table-head"><span class="t">Baccart A5-3C</span><span class="lim">Bet Limit</span><span class="c">Commission 0/7</span><span class="n">0/100</span></div>
    <div class="abs join">JOIN</div>
    <svg class="abs" style="left:0;top:54px" width="350" height="86"><use href="#felt"/></svg>
    <div class="abs seats"><svg class="abs" style="left:0;top:4px" width="230" height="36"><use href="#seatrow"/></svg><span class="abs drop" style="left:241px"><svg width="28" height="20"><use href="#down"/></svg></span><span class="abs drop" style="left:292px"><svg width="28" height="20"><use href="#down"/></svg></span></div>
  </article>
  <article class="abs table" style="left:622px;top:540px">
    <div class="abs table-head"><span class="t">Baccart A5-3C</span><span class="lim">Bet Limit</span><span class="c">Commission 0/7</span><span class="n">0/100</span></div>
    <div class="abs join">JOIN</div>
    <svg class="abs" style="left:0;top:54px" width="350" height="86"><use href="#felt"/></svg>
    <div class="abs seats"><svg class="abs" style="left:0;top:4px" width="230" height="36"><use href="#seatrow"/></svg><span class="abs drop" style="left:241px"><svg width="28" height="20"><use href="#down"/></svg></span><span class="abs drop" style="left:292px"><svg width="28" height="20"><use href="#down"/></svg></span></div>
  </article>
  <article class="abs table" style="left:994px;top:540px">
    <div class="abs table-head"><span class="t">Baccart A5-3C</span><span class="lim">Bet Limit</span><span class="c">Commission 0/7</span><span class="n">0/100</span></div>
    <div class="abs join">JOIN</div>
    <svg class="abs" style="left:0;top:54px" width="350" height="86"><use href="#felt"/></svg>
    <div class="abs seats"><svg class="abs" style="left:0;top:4px" width="230" height="36"><use href="#seatrow"/></svg><span class="abs drop" style="left:241px"><svg width="28" height="20"><use href="#down"/></svg></span><span class="abs drop" style="left:292px"><svg width="28" height="20"><use href="#down"/></svg></span></div>
  </article>

  <footer class="abs balance-bar">
    <span class="balance-label">Balance</span>
    <span class="cur">$SGD<i>&lsaquo;</i></span>
    <span class="amount">999,999.999</span>
  </footer>
</div>
</body>
</html>
```